company name - KELBRIDGE AIRPORT TRANSFER.
include this information please .....25 YEARS EXPERIENCE / CARS+MPVS+MINIBUSES AVAILABLE - ALL AT SAME PRICE AT ANY TIME OF DAY. NO EXTRA HIDDEN CHARGES.

PRICES [ selection ] ......

DUNMARSH ....£100
PELLORN ....£130
VASKE...£55.00
ORMBRIDGE ...£60.00
WESTHALLOCK ...£100.00
NORTH FELWAY ...£100,00
QUAY AIRPORT ...£95.00

```html
<!DOCTYPE html>
<html lang="en">
<head>
<meta charset="utf-8">
<title>Kelbridge Airport Transfer</title>
<link rel="stylesheet" href="https://fonts.googleapis.com/css2?family=Oswald:wght@300;400&family=Open+Sans:wght@400&display=swap">
<style>
  :root {
    --hero-dark: #1e1410;
    --hero-brown: #5a3418;
    --hero-glow: #c9a22a;
    --white: #ffffff;
    --tick: #f5e21a;
    --band-yellow: #ffe600;
    --pin-orange: #f7941d;
    --ring-orange: #f5a03a;
    --label-ink: #1f1f1f;
  }
  * { margin: 0; padding: 0; box-sizing: border-box; }
  html, body { width: 1200px; height: 850px; overflow: hidden; background: var(--band-yellow); }
  .poster { position: relative; width: 1200px; height: 850px; overflow: hidden; }

  .hero {
    position: absolute; left: 0; top: 0; width: 1200px; height: 422px;
    background:
      radial-gradient(ellipse 300px 110px at 480px 190px, rgba(230,200,50,0.55), transparent 70%),
      radial-gradient(ellipse 380px 120px at 520px 320px, rgba(200,140,40,0.45), transparent 75%),
      linear-gradient(180deg, #8a5a30 0%, var(--hero-brown) 25%, #3a2414 60%, var(--hero-dark) 100%);
  }
  .hero-title {
    position: absolute; left: 0; top: 132px; width: 1200px; text-align: center;
    font-family: "Oswald", sans-serif; font-weight: 400; font-size: 76px; line-height: 100px;
    color: var(--white); letter-spacing: 0.5px;
    text-shadow: 0 3px 6px rgba(0,0,0,0.55);
  }
  .features {
    position: absolute; left: 0; top: 282px; width: 1200px;
    display: flex; justify-content: center; gap: 30px; list-style: none;
    font-family: "Oswald", sans-serif; font-weight: 300; font-size: 20px; line-height: 30px;
    color: var(--white);
  }
  .features li { display: flex; align-items: center; gap: 10px; }
  .features svg { width: 17px; height: 14px; }

  .prices { position: absolute; left: 0; top: 422px; width: 1200px; height: 428px; background: var(--band-yellow); }
  .stop {
    position: absolute; width: 200px; transform: translateX(-50%);
    display: flex; flex-direction: column; align-items: center;
    font-family: "Open Sans", sans-serif; font-size: 23px; line-height: 28px; color: var(--label-ink);
  }
  .stop.high { top: 26px; }
  .stop.low { top: 143px; }
  .pin { width: 28px; height: 50px; margin-bottom: 2px; }
  .photo {
    width: 140px; height: 140px; border-radius: 50%;
    border: 2px solid var(--ring-orange);
  }
  .stop-name { margin-top: 12px; }
  .photo.dunmarsh { background: linear-gradient(180deg, #8fbbe6 0%, #dfe8f0 45%, #7d8a96 75%, #4f5b66 100%); }
  .photo.pellorn { background: linear-gradient(180deg, #7fa9d6 0%, #a9c6e2 45%, #2c3440 70%, #3a4a6a 100%); }
  .photo.vaske { background: linear-gradient(160deg, #c9ccd2 0%, #e6e8ec 45%, #9aa3ae 100%); }
  .photo.ormbridge { background: linear-gradient(180deg, #a8c4e0 0%, #d8dde2 40%, #8c8e90 75%, #5f6164 100%); }
  .photo.westhallock { background: linear-gradient(180deg, #b8d0ea 0%, #e8e4dc 40%, #c4a887 70%, #9c8570 100%); }
  .photo.north-felway { background: linear-gradient(180deg, #6fa0d4 0%, #a9bed4 40%, #8a8478 75%, #6b5e52 100%); }
  .photo.quay-airport { background: linear-gradient(180deg, #2f6cc0 0%, #6f9bd6 40%, #5b6f86 70%, #9a9ea4 100%); }
</style>
</head>
<body>
<main class="poster">
  <header class="hero" role="img" aria-label="Blurred warm-toned photograph of a lit airport terminal interior">
  </header>
  <h1 class="hero-title">KELBRIDGE AIRPORT TRANSFER</h1>
  <ul class="features">
    <li><svg viewBox="0 0 17 14" aria-hidden="true"><path d="M1.5 7.5 L6 12 L15.5 2" fill="none" stroke="#f5e21a" stroke-width="3" stroke-linecap="round" stroke-linejoin="round"/></svg>25 YEARS EXPERIENCE</li>
    <li><svg viewBox="0 0 17 14" aria-hidden="true"><path d="M1.5 7.5 L6 12 L15.5 2" fill="none" stroke="#f5e21a" stroke-width="3" stroke-linecap="round" stroke-linejoin="round"/></svg>CARS+MPVS+MINIBUSES AVAILABLE</li>
    <li><svg viewBox="0 0 17 14" aria-hidden="true"><path d="M1.5 7.5 L6 12 L15.5 2" fill="none" stroke="#f5e21a" stroke-width="3" stroke-linecap="round" stroke-linejoin="round"/></svg>ALL AT SAME PRICE AT ANY TIME OF DAY</li>
    <li><svg viewBox="0 0 17 14" aria-hidden="true"><path d="M1.5 7.5 L6 12 L15.5 2" fill="none" stroke="#f5e21a" stroke-width="3" stroke-linecap="round" stroke-linejoin="round"/></svg>NO EXTRA HIDDEN CHARGES</li>
  </ul>

  <section class="prices">
    <div class="stop high" style="left:93px">
      <svg class="pin" viewBox="0 0 28 50" aria-hidden="true"><path d="M14 50 C11 40 1 28 1 14 A13 13 0 0 1 27 14 C27 28 17 40 14 50 Z" fill="#f7941d"/><circle cx="14" cy="14" r="5.5" fill="#ffe600"/></svg>
      <div class="photo dunmarsh" role="img" aria-label="Airliner parked at a terminal gate under a blue sky"></div>
      <div class="stop-name">DUNMARSH</div><div class="stop-price">£100</div>
    </div>
    <div class="stop low" style="left:263px">
      <svg class="pin" viewBox="0 0 28 50" aria-hidden="true"><path d="M14 50 C11 40 1 28 1 14 A13 13 0 0 1 27 14 C27 28 17 40 14 50 Z" fill="#f7941d"/><circle cx="14" cy="14" r="5.5" fill="#ffe600"/></svg>
      <div class="photo pellorn" role="img" aria-label="Plane landing above an airport sign"></div>
      <div class="stop-name">PELLORN</div><div class="stop-price">£130</div>
    </div>
    <div class="stop high" style="left:410px">
      <svg class="pin" viewBox="0 0 28 50" aria-hidden="true"><path d="M14 50 C11 40 1 28 1 14 A13 13 0 0 1 27 14 C27 28 17 40 14 50 Z" fill="#f7941d"/><circle cx="14" cy="14" r="5.5" fill="#ffe600"/></svg>
      <div class="photo vaske" role="img" aria-label="Close view of lettering on a terminal facade"></div>
      <div class="stop-name">VASKE</div><div class="stop-price">£55</div>
    </div>
    <div class="stop low" style="left:565px">
      <svg class="pin" viewBox="0 0 28 50" aria-hidden="true"><path d="M14 50 C11 40 1 28 1 14 A13 13 0 0 1 27 14 C27 28 17 40 14 50 Z" fill="#f7941d"/><circle cx="14" cy="14" r="5.5" fill="#ffe600"/></svg>
      <div class="photo ormbridge" role="img" aria-label="Terminal entrance canopy with cars at the drop-off lane"></div>
      <div class="stop-name">ORMBRIDGE</div><div class="stop-price">£60</div>
    </div>
    <div class="stop high" style="left:743px">
      <svg class="pin" viewBox="0 0 28 50" aria-hidden="true"><path d="M14 50 C11 40 1 28 1 14 A13 13 0 0 1 27 14 C27 28 17 40 14 50 Z" fill="#f7941d"/><circle cx="14" cy="14" r="5.5" fill="#ffe600"/></svg>
      <div class="photo westhallock" role="img" aria-label="Domed civic building on a city square"></div>
      <div class="stop-name">WESTHALLOCK</div><div class="stop-price">£100</div>
    </div>
    <div class="stop low" style="left:926px">
      <svg class="pin" viewBox="0 0 28 50" aria-hidden="true"><path d="M14 50 C11 40 1 28 1 14 A13 13 0 0 1 27 14 C27 28 17 40 14 50 Z" fill="#f7941d"/><circle cx="14" cy="14" r="5.5" fill="#ffe600"/></svg>
      <div class="photo north-felway" role="img" aria-label="Gothic town hall on a historic market square"></div>
      <div class="stop-name">NORTH FELWAY</div><div class="stop-price">£100</div>
    </div>
    <div class="stop high" style="left:1108px">
      <svg class="pin" viewBox="0 0 28 50" aria-hidden="true"><path d="M14 50 C11 40 1 28 1 14 A13 13 0 0 1 27 14 C27 28 17 40 14 50 Z" fill="#f7941d"/><circle cx="14" cy="14" r="5.5" fill="#ffe600"/></svg>
      <div class="photo quay-airport" role="img" aria-label="Modern glass terminal building with a crossing in front"></div>
      <div class="stop-name">QUAY AIRPORT</div><div class="stop-price">£95</div>
    </div>
  </section>
</main>
</body>
</html>
```